Letterhead to Introduce a 'Sister' Company.

What I am needing is a design for a letter head to introduce our current customers base of (KT Alarm) customers to our new service, 'Kestrel Tide Solar Brokers'

```html
<!DOCTYPE html>
<html lang="en">
<head>
<meta charset="utf-8">
<title>Kestrel Tide Solar Brokers – Letterhead</title>
<link rel="stylesheet" href="https://fonts.googleapis.com/css2?family=Open+Sans:wght@400;600&family=Lato:wght@400;700&family=Arimo:wght@400&display=swap">
<style>
  :root {
    --paper: #ffffff;
    --ink: #3a3a3a;
    --ink-soft: #4a4a4a;
    --navy: #143f7a;
    --solar: #f39a1c;
    --rule-grey: #9a9a9a;
  }
  * { margin: 0; padding: 0; box-sizing: border-box; }
  html, body { width: 1040px; height: 1200px; overflow: hidden; background: var(--paper); }
  .letterhead {
    position: relative; width: 1040px; height: 1200px; background: var(--paper);
    font-family: "Open Sans", Arial, sans-serif; color: var(--ink);
  }
  .brand {
    position: absolute; left: 100px; top: 40px;
    display: flex; align-items: center; gap: 14px;
  }
  .brand__dot { width: 44px; height: 44px; border-radius: 50%; background: var(--solar); flex: none; }
  .brand__name {
    font-family: "Open Sans", Arial, sans-serif; font-weight: 600; color: var(--navy);
    font-size: 26px; line-height: 1.15; letter-spacing: 0.5px;
  }
  .contact {
    position: absolute; left: 707px; top: 22px; height: 82px;
    border-left: 1px solid var(--rule-grey); padding-left: 14px;
    font-family: "Arimo", Arial, sans-serif; font-size: 16px; color: #1b1b1b; line-height: 20px;
  }
  .contact__item { display: flex; align-items: center; gap: 6px; }
  .contact__item svg { width: 13px; height: 13px; flex: none; }
  .letter { position: absolute; left: 97px; width: 840px; font-size: 15.5px; }
  .letter__date { top: 218px; }
  .letter__recipient { top: 254px; line-height: 19px; }
  .letter__greeting { top: 358px; }
  .letter__body { top: 410px; line-height: 27px; text-align: justify; hyphens: auto; }
  .letter__body p + p { margin-top: 27px; }
  .letter__closing { top: 818px; }
  .signature { position: absolute; left: 97px; top: 892px; }
  .signature__name { font-size: 19px; font-weight: 600; color: #2a2a2a; }
  .signature__role { font-size: 15.5px; margin-top: 4px; }
  .footer { position: absolute; left: 0; top: 1100px; width: 1040px; }
  .footer__rule { position: absolute; height: 2px; background: var(--solar); }
  .footer__mark {
    position: absolute; left: 0; width: 1040px; top: 0; text-align: center;
    font-family: "Lato", Arial, sans-serif; font-weight: 700; font-size: 30px; color: var(--navy);
    letter-spacing: 1px;
  }
  .footer__address {
    position: absolute; left: 0; width: 1040px; top: 44px; text-align: center;
    font-family: "Lato", Arial, sans-serif; font-size: 20px; color: #1b1b1b;
  }
</style>
</head>
<body>
<main class="letterhead">
  <header>
    <div class="brand">
      <span class="brand__dot"></span>
      <span class="brand__name">Kestrel Tide<br>Solar Brokers</span>
    </div>
    <address class="contact" style="font-style:normal">
      <div class="contact__item">
        <svg viewBox="0 0 16 16"><path d="M3 1l3 3-2 2c1 2 3 4 5 5l2-2 3 3-2 3C7 15 1 9 0 4z" fill="var(--navy)"/></svg>
        044-555 210 347
      </div>
      <div class="contact__item">
        <svg viewBox="0 0 16 16"><rect x="4" y="1" width="8" height="14" rx="1.5" fill="none" stroke="var(--navy)" stroke-width="1.8"/></svg>
        044-555 210 347
      </div>
      <div class="contact__item">
        <svg viewBox="0 0 16 16"><rect x="1" y="3" width="14" height="10" fill="var(--navy)"/><path d="M1 3l7 6 7-6" fill="none" stroke="#fff" stroke-width="1.2"/></svg>
        hello@kestreltide.net
      </div>
      <div class="contact__item">
        <svg viewBox="0 0 16 16"><circle cx="8" cy="8" r="6.5" fill="none" stroke="var(--navy)" stroke-width="1.4"/><ellipse cx="8" cy="8" rx="3" ry="6.5" fill="none" stroke="var(--navy)" stroke-width="1.2"/><path d="M1.5 8h13" stroke="var(--navy)" stroke-width="1.2"/></svg>
        www.kestreltidesolar.net
      </div>
    </address>
  </header>

  <p class="letter letter__date">Issuing Date: May 5, 2018</p>
  <p class="letter letter__recipient">Name Of Employee Mr. XYZABC<br>Address of Employee<br>Address Line 2 etc..</p>
  <p class="letter letter__greeting">Dear Mr.XYZABC</p>

  <section class="letter letter__body">
    <p>Lorem Ipsum has been the industry's standard dummy text ever since the 1500s, when an unknown printer took a galley of type and scrambled it to make a type specimen book. It has survived not only five centuries, but also the leap into electronic typesetting, remaining essentially unchanged. It was popularised in the 1960s with the release of Lettaform sheets containing Lorem Ipsum passages, and more recently with desktop publishing software like Pagewright including versions of Lorem Ipsum.</p>
    <p>Lorem Ipsum is simply dummy text of the printing and typesetting industry. Lorem Ipsum has been the industry's standard dummy text ever since the 1500s, when an unknown printer took a galley of type and scrambled it to make a type specimen book.</p>
    <p>It has survived not only five centuries, but also the leap into electronic typesetting, remaining essentially unchanged. It was popularised in the 1960s with the release of Lettaform sheets containing Lorem IpsumIpsum passages.</p>
  </section>

  <p class="letter letter__closing">Yours Sincerely</p>
  <div class="signature">
    <p class="signature__name">Marcus Ellery</p>
    <p class="signature__role">Managing Director</p>
  </div>

  <footer class="footer">
    <span class="footer__rule" style="left:97px;width:277px;top:22px"></span>
    <span class="footer__rule" style="left:705px;width:235px;top:22px"></span>
    <div class="footer__mark">KT Alarm</div>
    <p class="footer__address">421, Address line here,&nbsp; dummy code 45452 Country Name</p>
    <span class="footer__rule" style="left:97px;width:849px;top:77px"></span>
  </footer>
</main>
</body>
</html>
```